Business card for a young aspring actress

My daughter is 18 and just starting out on her profession as an actress. She is a member of the Harbour Young Players and has already had some extras work and a featured role in an upcoming Feature film.

She wants/needs a card that she can have to hand to give to those she comes into contact with in the theatre, TV and film industries.

We are thinking that it may be double sided with an impact side including a picture of her and her name etc with the reverse holding contact and other details.

She wants to go by the name Maya Louise Brennick.

She has done a little modelling but sees herself as an actress.

She can be seen in this video
http://www.oakvalepark-academy.org/videos/be0881e4276ee2512c50a07f907c1d03?width=640&height=480

Target Market(s)

Anyone she comes into contact with in theatre TV and film industries.

Industry/Entity Type

Business

Requirements
Nice to have
• She has email and a website www.mayabrennick.com She is quite a connected girl

```html
<!DOCTYPE html>
<html lang="en">
<head>
<meta charset="utf-8">
<title>Maya Louise Brennick – Actress Business Card</title>
<link rel="stylesheet" href="https://fonts.googleapis.com/css2?family=Share+Tech+Mono&family=Jost:ital,wght@0,400;0,600;1,400&display=swap">
<style>
  :root {
    --rose: #d77a80;
    --band-grey: #c9c7c8;
    --white: #ffffff;
    --portrait-light: #e6e6e6;
    --portrait-mid: #a9a9a9;
    --portrait-dark: #4a4a4a;
  }
  * { margin: 0; padding: 0; box-sizing: border-box; }
  html, body {
    width: 1200px;
    height: 388px;
    overflow: hidden;
    background: var(--white);
  }
  .card {
    position: relative;
    width: 1200px;
    height: 388px;
    overflow: hidden;
    font-family: "Jost", sans-serif;
    color: var(--white);
  }
  .portrait {
    position: absolute;
    left: 0; top: 0;
    width: 516px;
    height: 388px;
    background:
      radial-gradient(ellipse 60% 75% at 60% 45%, var(--portrait-light) 0%, #cfcfcf 55%, transparent 80%),
      linear-gradient(90deg, var(--portrait-dark) 0%, var(--portrait-mid) 25%, #d8d8d8 55%, #bdbdbd 100%);
  }
  .name-band {
    position: absolute;
    left: 516px; top: 0;
    width: 84px;
    height: 388px;
    background: var(--band-grey);
  }
  .band-name,
  .band-role {
    position: absolute;
    transform: rotate(-90deg);
    transform-origin: left top;
    white-space: nowrap;
    color: var(--white);
  }
  .band-name {
    left: 530px;
    top: 368px;
    font-family: "Share Tech Mono", monospace;
    font-size: 23px;
    line-height: 30px;
    letter-spacing: 4.6px;
  }
  .band-role {
    left: 565px;
    top: 228px;
    font-family: "Jost", sans-serif;
    font-style: italic;
    font-size: 14px;
    line-height: 20px;
    letter-spacing: 0.5px;
  }
  .details {
    position: absolute;
    left: 600px; top: 0;
    width: 600px;
    height: 388px;
    background: var(--rose);
  }
  .details-name {
    position: absolute;
    left: 51px;
    top: 108px;
    font-family: "Share Tech Mono", monospace;
    font-weight: 400;
    font-size: 33px;
    line-height: 36px;
    letter-spacing: 4.4px;
  }
  .details-email {
    position: absolute;
    left: 49px;
    top: 169px;
    font-size: 20px;
    line-height: 26px;
  }
  .contact {
    position: absolute;
    top: 273px;
    font-size: 16.5px;
    line-height: 24px;
    list-style: none;
  }
  .contact-online { left: 49px; }
  .contact-online .website { font-weight: 600; }
  .contact-postal { left: 290px; }
  .contact-postal .label { display: inline-block; width: 84px; }
</style>
</head>
<body>
  <main class="card">
    <div class="portrait" role="img" aria-label="Black and white close-up portrait photograph of the actress"></div>

    <div class="name-band"></div>
    <p class="band-name">Maya Louise Brennick</p>
    <p class="band-role">Actress</p>

    <section class="details">
      <h1 class="details-name">Maya Louise Brennick</h1>
      <p class="details-email">name@domain.com</p>

      <ul class="contact contact-online">
        <li class="website">www.domainname.tv</li>
        <li>F: facebookaccountname</li>
        <li>T: twitteraccountname</li>
      </ul>

      <ul class="contact contact-postal">
        <li><span class="label">Mobile</span>+11 22 3344 567</li>
        <li>Adressline 1</li>
        <li>Adressline 2</li>
      </ul>
    </section>
  </main>
</body>
</html>
```